Sole trader requires buisness card / company logo for mining and aviation

I require a business card and logo design having the following requirements;
Kestrel Airframe and Plant Services
Owner: Martin Hollis
Ph: 0491570156
E: martin-r-hollis@brolgamail.com.au

Logo should include a basic aircraft image and an image of an item of mining machinery either a dump truck or large excavator, but keeping in mind that the image is to be transferred onto clothing embroidery.

```html
<!DOCTYPE html>
<html lang="en">
<head>
<meta charset="utf-8">
<title>Kestrel Airframe and Plant Services – Business Cards</title>
<link rel="stylesheet" href="https://fonts.googleapis.com/css2?family=Open+Sans:wght@400;600;700&display=swap">
<style>
  :root {
    --canvas: #e9e9e7;
    --card-white: #ffffff;
    --accent-blue: #3b97d6;
    --accent-green: #8dc63f;
    --mark-grey: #555555;
    --text-light: #ffffff;
    --shadow: rgba(0, 0, 0, 0.18);
  }
  * { box-sizing: border-box; margin: 0; padding: 0; }
  html, body {
    width: 1200px;
    height: 1000px;
    overflow: hidden;
    background: var(--canvas);
    font-family: "Open Sans", Arial, sans-serif;
  }
  .sheet {
    position: relative;
    width: 1200px;
    height: 1000px;
  }
  .card {
    position: absolute;
    width: 540px;
    height: 320px;
    border-radius: 22px;
    overflow: hidden;
    box-shadow: 0 6px 18px var(--shadow);
  }
  .card--front-blue  { left: 40px;  top: 120px; --accent: var(--accent-blue); }
  .card--back-grey   { left: 40px;  top: 560px; --mark: var(--mark-grey); }
  .card--front-green { left: 620px; top: 120px; --accent: var(--accent-green); }
  .card--back-green  { left: 620px; top: 560px; --mark: var(--accent-green); }

  /* Front side */
  .card--front { background: var(--accent); }
  .card__band {
    position: absolute;
    left: 0;
    top: 0;
    width: 540px;
    height: 320px;
  }
  .card__content {
    position: absolute;
    left: 0;
    top: 56px;
    width: 540px;
    height: 190px;
    padding: 0 26px 0 34px;
    display: flex;
    align-items: center;
  }
  .wordmark {
    display: flex;
    align-items: center;
    gap: 10px;
  }
  .wordmark__square {
    flex: none;
    width: 16px;
    height: 16px;
  }
  .wordmark__name {
    font-weight: 700;
    text-transform: uppercase;
    letter-spacing: 0.4px;
    line-height: 1.2;
  }
  .card--front .wordmark {
    flex: none;
    width: 200px;
    color: var(--text-light);
  }
  .card--front .wordmark__square { background: var(--text-light); }
  .card--front .wordmark__name { font-size: 16px; }

  .contact {
    flex: 1;
    min-width: 0;
    margin-left: 34px;
    color: var(--text-light);
  }
  .contact__name {
    font-size: 20px;
    font-weight: 600;
    color: var(--accent);
    margin-bottom: 22px;
  }
  .contact__line {
    display: flex;
    align-items: center;
    gap: 8px;
    font-size: 12.5px;
    line-height: 1.7;
    white-space: nowrap;
  }
  .contact__icon {
    flex: none;
    width: 12px;
    height: 12px;
    fill: var(--accent);
  }

  /* Back side */
  .card--back {
    background: var(--card-white);
    display: flex;
    align-items: center;
    justify-content: center;
  }
  .card--back .wordmark {
    width: 380px;
    color: var(--mark);
    gap: 14px;
  }
  .card--back .wordmark__square {
    width: 26px;
    height: 26px;
    background: var(--mark);
  }
  .card--back .wordmark__name { font-size: 26px; }
</style>
</head>
<body>
<main class="sheet">

  <section class="card card--front card--front-blue" aria-label="Business card front, blue">
    <svg class="card__band" viewBox="0 0 540 320" aria-hidden="true">
      <defs>
        <linearGradient id="darkBandBlue" x1="0" y1="0" x2="0" y2="1">
          <stop offset="0" stop-color="#262626"/>
          <stop offset="1" stop-color="#161616"/>
        </linearGradient>
      </defs>
      <path fill="url(#darkBandBlue)" d="M0 58 L60 52 L130 60 L210 48 L290 56 L370 44 L450 52 L540 40 L540 238 L460 250 L380 242 L300 256 L220 248 L140 262 L60 254 L0 264 Z"/>
    </svg>
    <div class="card__content">
      <div class="wordmark">
        <span class="wordmark__square"></span>
        <span class="wordmark__name">Kestrel Airframe and Plant Services</span>
      </div>
      <div class="contact">
        <p class="contact__name">Martin Hollis</p>
        <p class="contact__line">
          <svg class="contact__icon" viewBox="0 0 16 16" aria-hidden="true"><path d="M3.6 1.2l2.3 2.6-1.3 1.9c.9 2 2.6 3.7 4.6 4.6l1.9-1.3 2.6 2.3-1.3 2.4C7.5 14.6 1.4 8.5 1.2 3.7z"/></svg>
          0491570156
        </p>
        <p class="contact__line">
          <svg class="contact__icon" viewBox="0 0 16 16" aria-hidden="true"><path d="M1 3h14v10H1z M2 4.2v.6l6 4 6-4v-.6z" fill-rule="evenodd"/></svg>
          martin-r-hollis@brolgamail.com.au
        </p>
      </div>
    </div>
  </section>

  <section class="card card--back card--back-grey" aria-label="Business card back, grey">
    <div class="wordmark">
      <span class="wordmark__square"></span>
      <span class="wordmark__name">Kestrel Airframe and Plant Services</span>
    </div>
  </section>

  <section class="card card--front card--front-green" aria-label="Business card front, green">
    <svg class="card__band" viewBox="0 0 540 320" aria-hidden="true">
      <defs>
        <linearGradient id="darkBandGreen" x1="0" y1="0" x2="0" y2="1">
          <stop offset="0" stop-color="#262626"/>
          <stop offset="1" stop-color="#161616"/>
        </linearGradient>
      </defs>
      <path fill="url(#darkBandGreen)" d="M0 58 L60 52 L130 60 L210 48 L290 56 L370 44 L450 52 L540 40 L540 238 L460 250 L380 242 L300 256 L220 248 L140 262 L60 254 L0 264 Z"/>
    </svg>
    <div class="card__content">
      <div class="wordmark">
        <span class="wordmark__square"></span>
        <span class="wordmark__name">Kestrel Airframe and Plant Services</span>
      </div>
      <div class="contact">
        <p class="contact__name">Martin Hollis</p>
        <p class="contact__line">
          <svg class="contact__icon" viewBox="0 0 16 16" aria-hidden="true"><path d="M3.6 1.2l2.3 2.6-1.3 1.9c.9 2 2.6 3.7 4.6 4.6l1.9-1.3 2.6 2.3-1.3 2.4C7.5 14.6 1.4 8.5 1.2 3.7z"/></svg>
          0491570156
        </p>
        <p class="contact__line">
          <svg class="contact__icon" viewBox="0 0 16 16" aria-hidden="true"><path d="M1 3h14v10H1z M2 4.2v.6l6 4 6-4v-.6z" fill-rule="evenodd"/></svg>
          martin-r-hollis@brolgamail.com.au
        </p>
      </div>
    </div>
  </section>

  <section class="card card--back card--back-green" aria-label="Business card back, green">
    <div class="wordmark">
      <span class="wordmark__square"></span>
      <span class="wordmark__name">Kestrel Airframe and Plant Services</span>
    </div>
  </section>

</main>
</body>
</html>
```